Design a business card & stationary for a mortgage company

We are looking for a good looking business card design for our mortgage company that includes our logo. We received a free design as part of our logo project but we don't love it. The company is called "Pinecrest Mortgage Company" so we like waves and lighthouses. The logo should be included. We have a version in both vertical and horizontal that we have provided.

Industry/Entity Type

Finance

Contact Information for Business Card

This should include our new logo file

Requirements
Must have
• 3. The details you'd like on the card - name, title, phone, email, website, address, social media handles etc.
1. Marcus Hale
Vice President
732-419-6253
Fax 888-304-2918
mhale@pinecrestmortgage.example
NMLS 47162 - Company NMLS 61290
18 Larkin Ave
Bayview Harbor, NJ 08614

```html
<!DOCTYPE html>
<html lang="en">
<head>
<meta charset="UTF-8">
<title>Pinecrest Mortgage Company – Business Card</title>
<link href="https://fonts.googleapis.com/css2?family=Montserrat:wght@400;500;700&display=swap" rel="stylesheet">
<style>
  :root {
    --canvas: #e9ecef;
    --navy: #0f5594;
    --navy-deep: #0b4a86;
    --sky: #1496dc;
    --ink: #124f8c;
    --white: #ffffff;
  }
  * { box-sizing: border-box; margin: 0; padding: 0; }
  html, body { width: 1200px; height: 900px; overflow: hidden; }
  body {
    background: var(--canvas);
    font-family: "Montserrat", Arial, sans-serif;
    display: flex; flex-direction: column; align-items: center; justify-content: center;
    gap: 36px;
  }
  .card {
    position: relative;
    width: 700px; height: 400px;
    border-radius: 18px;
    overflow: hidden;
    box-shadow: 0 8px 24px rgba(0,0,0,.18);
  }

  /* Back */
  .card-back {
    background: linear-gradient(135deg, var(--navy-deep), var(--navy) 60%, #1463a6);
  }
  .back-brand {
    position: absolute; right: 60px; top: 150px;
    text-align: right; color: var(--white);
  }
  .brand-name {
    font-weight: 500; letter-spacing: .06em; text-transform: uppercase;
    font-size: 26px; line-height: 1.2;
  }
  .brand-name .dot {
    display: inline-block; width: 12px; height: 12px; border-radius: 50%;
    background: currentColor; margin-right: 10px; vertical-align: middle;
  }
  .brand-nmls {
    margin-top: 10px; font-size: 12px; letter-spacing: .4em; font-weight: 500;
  }

  /* Front */
  .card-front { background: var(--white); }
  .front-shape { position: absolute; inset: 0; }
  .front-brand {
    position: absolute; left: 36px; top: 175px; width: 260px;
    text-align: center; color: var(--ink);
  }
  .front-brand .brand-name { font-size: 20px; }
  .front-brand .brand-nmls { font-size: 10px; }

  .details {
    position: absolute; left: 400px; top: 70px; width: 285px; color: var(--white);
  }
  .person-name { font-weight: 700; font-size: 24px; letter-spacing: .04em; text-transform: uppercase; }
  .person-title { font-size: 14px; margin-top: 2px; }
  .rule { height: 1px; background: var(--sky); margin: 14px 0 16px; width: 250px; }
  .contact-list { list-style: none; font-size: 13px; line-height: 1.7; }
  .contact-list li { display: flex; align-items: flex-start; gap: 8px; white-space: nowrap; }
  .contact-list svg { width: 12px; height: 12px; margin-top: 5px; flex: none; fill: var(--white); }
  .contact-list .address { margin-top: 8px; line-height: 1.45; }
</style>
</head>
<body>

  <section class="card card-back" aria-label="Card back">
    <div class="back-brand">
      <div class="brand-name"><span class="dot"></span>Pinecrest Mortgage Company</div>
      <div class="brand-nmls">NMLS 61290</div>
    </div>
  </section>

  <section class="card card-front" aria-label="Card front">
    <svg class="front-shape" viewBox="0 0 700 400" preserveAspectRatio="none">
      <path d="M300 0 C360 10 340 140 350 220 C360 330 420 395 520 400 L700 400 L700 0 Z" fill="#1496dc"/>
      <path d="M315 0 C372 14 356 140 366 220 C378 320 430 385 530 400 L700 400 L700 0 Z" fill="#0f5594"/>
    </svg>

    <div class="front-brand">
      <div class="brand-name">Pinecrest Mortgage Company</div>
      <div class="brand-nmls">NMLS 61290</div>
    </div>

    <div class="details">
      <h1 class="person-name">Marcus Hale</h1>
      <p class="person-title">Vice President</p>
      <div class="rule"></div>
      <ul class="contact-list">
        <li><svg viewBox="0 0 24 24"><path d="M6.6 10.8a15 15 0 0 0 6.6 6.6l2.2-2.2a1 1 0 0 1 1-.25 11.4 11.4 0 0 0 3.6.57 1 1 0 0 1 1 1V20a1 1 0 0 1-1 1A17 17 0 0 1 3 4a1 1 0 0 1 1-1h3.5a1 1 0 0 1 1 1c0 1.25.2 2.45.57 3.57a1 1 0 0 1-.25 1z"/></svg>732-419-6253</li>
        <li><svg viewBox="0 0 24 24"><path d="M6 2h10v5H6zM3 8h18v9h-3v5H6v-5H3zm5 7v5h8v-5z"/></svg>888-304-2918</li>
        <li><svg viewBox="0 0 24 24"><path d="M2 5h20v14H2zm2 2v.5l8 5 8-5V7l-8 5z"/></svg>mhale@pinecrestmortgage.example</li>
        <li><svg viewBox="0 0 24 24"><circle cx="12" cy="12" r="10"/></svg>www.pinecrestmortgage.example</li>
        <li class="address"><svg viewBox="0 0 24 24"><path d="M12 2a7 7 0 0 0-7 7c0 5 7 13 7 13s7-8 7-13a7 7 0 0 0-7-7zm0 9.5A2.5 2.5 0 1 1 12 6.5a2.5 2.5 0 0 1 0 5z"/></svg><span>NMLS 47162 - Company NMLS 61290<br>18 Larkin Ave<br>Bayview Harbor, NJ 08614</span></li>
      </ul>
    </div>
  </section>

</body>
</html>
```